Note/Card sent to show appreciation to partners who worked with us to improve local communities

I'd like a simple note/card designed for a wide audience. Originally, I called this a "Thanksgiving Card," but it's really just a card to be sent around Thanksgiving, not specifically celebrating the Thanksgiving holiday. We plan to send the card out just prior to Thanksgiving 2017 (Nov. 24, 2017). I work at a regulated electric utility, and we'd like to say thank you to the many stakeholders who we partner with throughout the year to support initiatives that help to improve our state and create opportunities for economic growth. I'm interested mostly in the design of the card, not the simple verbiage on the inside.
Target Market(s)
Customers, charitable foundations, nonprofits, advocacy groups, industry associations, friends

```html
<!DOCTYPE html>
<html lang="en">
<head>
<meta charset="utf-8">
<title>Thanks Card</title>
<link rel="stylesheet" href="https://fonts.googleapis.com/css2?family=Tinos&display=swap">
<style>
  :root {
    --card-orange: #f7941d;
    --brand-faint: #fdb64f;
    --thanks-purple: #662d91;
    --text-white: #ffffff;
    --guide-line: #3a2a1a;
  }
  html, body {
    margin: 0;
    padding: 0;
    width: 1200px;
    height: 849px;
    overflow: hidden;
    background: #ffffff;
  }
  .card {
    position: relative;
    width: 1200px;
    height: 849px;
    background: var(--card-orange);
    overflow: hidden;
    font-family: "Tinos", "Times New Roman", serif;
  }
  .trim-guide {
    position: absolute;
    inset: 6px;
    border: 1px dashed var(--guide-line);
    z-index: 5;
  }
  .fold-guide {
    position: absolute;
    left: 600px;
    top: 6px;
    bottom: 6px;
    border-left: 1px dashed var(--guide-line);
    z-index: 5;
  }
  .sweep {
    position: absolute;
    inset: 0;
    width: 1200px;
    height: 849px;
  }
  .sweep--under { z-index: 1; }
  .sweep--over { z-index: 3; pointer-events: none; }
  .brand-faint {
    position: absolute;
    left: 60px;
    top: 420px;
    width: 460px;
    text-align: center;
    color: var(--brand-faint);
    font-size: 64px;
    line-height: 1.05;
    z-index: 2;
  }
  .brand-front {
    position: absolute;
    left: 640px;
    top: 115px;
    width: 300px;
    text-align: center;
    color: var(--text-white);
    font-size: 34px;
    line-height: 1.1;
    z-index: 2;
  }
  .thanks-panel {
    position: absolute;
    left: 660px;
    top: 259px;
    width: 473px;
    height: 425px;
    background: var(--thanks-purple);
    z-index: 2;
    display: flex;
    align-items: center;
    justify-content: center;
  }
  .thanks-word {
    margin: 0;
    color: var(--text-white);
    font-size: 142px;
    font-weight: 400;
    line-height: 1;
    letter-spacing: -1px;
  }
</style>
</head>
<body>
  <main class="card">
    <svg class="sweep sweep--under" viewBox="0 0 1200 849" aria-hidden="true">
      <defs>
        <linearGradient id="sweepGlow" x1="0" y1="1" x2="1" y2="0">
          <stop offset="0" stop-color="#fff" stop-opacity="0"/>
          <stop offset="0.45" stop-color="#fff" stop-opacity="0.55"/>
          <stop offset="1" stop-color="#fff" stop-opacity="0.85"/>
        </linearGradient>
        <linearGradient id="edgeGlow" x1="0" y1="0" x2="1" y2="0">
          <stop offset="0" stop-color="#fff" stop-opacity="0.1"/>
          <stop offset="1" stop-color="#fff" stop-opacity="0.75"/>
        </linearGradient>
      </defs>
      <path d="M0 815 Q 560 800 880 640 Q 1140 470 1070 0 L 1200 0 L 1200 849 L 0 849 Z" fill="url(#sweepGlow)"/>
      <path d="M0 835 Q 600 830 940 660 Q 1190 500 1120 0 L 1200 0 L 1200 849 L 0 849 Z" fill="var(--card-orange)" opacity="0.7"/>
      <path d="M1055 0 Q 1130 360 930 849 L 1200 849 L 1200 0 Z" fill="url(#edgeGlow)" opacity="0.6"/>
    </svg>

    <div class="brand-faint">Brightline<br>Power</div>
    <div class="brand-front">Brightline Power</div>

    <section class="thanks-panel">
      <h1 class="thanks-word">thanks</h1>
    </section>

    <svg class="sweep sweep--over" viewBox="0 0 1200 849" aria-hidden="true">
      <defs>
        <linearGradient id="panelSheen" x1="0" y1="1" x2="1" y2="0">
          <stop offset="0" stop-color="#fff" stop-opacity="0"/>
          <stop offset="1" stop-color="#fff" stop-opacity="0.35"/>
        </linearGradient>
      </defs>
      <path d="M740 684 Q 1000 520 1060 259 L 1133 259 L 1133 684 Z" fill="url(#panelSheen)"/>
    </svg>

    <div class="trim-guide"></div>
    <div class="fold-guide"></div>
  </main>
</body>
</html>
```